Research, Writing and Editing business needs a Business Card Design

I need a business card design for a new company based in Melbourne called The Amber Advisory Collective. We provide research, writing and editing services. The company logo is attached, but I am open to your creative designs for business cards with the logo. As you will note, there are two potential logos. Feel free to use either of the logos.

The overall look I am hoping for is sleek, sophisticated, feminine and elegant.

Thanks in advance for your efforts.

Target Market(s)

Business professionals, academics and students

Industry/Entity Type

Business

Font styles to use
Serif
Script

Colors

Designer to choose colors to be used in the design.

Requirements
Must have
• The Amber Advisory Collective
Dr Nola Fenwick

M: 0482 593 247
E: nola@theamberadvisorycollective.com.au
W: theamberadvisorycollective.com.au
Nice to have
• Research | Writing | Editing

```html
<!DOCTYPE html>
<html lang="en">
<head>
<meta charset="utf-8">
<title>The Amber Advisory Collective – Business Card</title>
<link href="https://fonts.googleapis.com/css2?family=Cinzel:wght@500&family=Montserrat:wght@400;600&display=swap" rel="stylesheet">
<style>
  :root {
    --backdrop: #dcdcdc;
    --paper: #f4f4f3;
    --ink: #111111;
    --text: #1c1c1c;
  }
  * { margin: 0; padding: 0; box-sizing: border-box; }
  html, body { width: 1200px; height: 720px; overflow: hidden; }
  body {
    background: var(--backdrop);
    font-family: "Montserrat", Arial, sans-serif;
    color: var(--text);
    position: relative;
  }
  .card {
    position: absolute;
    top: 242px;
    width: 420px;
    height: 238px;
    background: var(--paper);
    overflow: hidden;
  }
  .card--front { left: 147px; }
  .card--back { left: 633px; }
  .quill-area {
    position: absolute;
    top: 0; left: 0;
    width: 420px; height: 238px;
  }
  .wordmark {
    font-family: "Cinzel", Georgia, serif;
    font-weight: 500;
    color: var(--ink);
    letter-spacing: 0.06em;
    line-height: 1.25;
  }
  .card--front .wordmark {
    position: absolute;
    left: 24px; top: 110px;
    font-size: 17px;
    width: 200px;
  }
  .services {
    position: absolute;
    left: 22px; top: 174px;
    font-size: 13px;
    letter-spacing: 0.01em;
  }
  .card--back .wordmark {
    position: absolute;
    right: 32px; top: 56px;
    font-size: 13px;
    text-align: right;
    width: 180px;
  }
  .holder {
    position: absolute;
    right: 34px; top: 150px;
    font-size: 12.5px;
    font-weight: 600;
  }
  .contacts {
    position: absolute;
    right: 30px; top: 182px;
    list-style: none;
    font-size: 9.2px;
    line-height: 13px;
    text-align: right;
  }
  .contacts li { display: flex; justify-content: flex-end; align-items: center; gap: 9px; }
  .contacts svg { width: 10px; height: 9px; flex: none; }
</style>
</head>
<body>

<section class="card card--front" aria-label="Card front">
  <svg class="quill-area" viewBox="0 0 420 238" role="img" aria-label="Large black quill feather illustration">
    <path d="M196 0 L420 0 L420 238 L404 238 C398 170 340 70 196 0 Z" fill="var(--ink)"/>
  </svg>
  <div class="wordmark">The Amber Advisory Collective</div>
  <p class="services">Research | Writing | Editing</p>
</section>

<section class="card card--back" aria-label="Card back">
  <svg class="quill-area" viewBox="0 0 420 238" role="img" aria-label="Large black quill feather illustration">
    <path d="M0 0 L226 0 C130 40 36 120 6 238 L0 238 Z" fill="var(--ink)"/>
  </svg>
  <div class="wordmark">The Amber Advisory Collective</div>
  <p class="holder">Dr Nola Fenwick</p>
  <ul class="contacts">
    <li><span>0482 593 247</span>
      <svg viewBox="0 0 10 9" aria-hidden="true"><path d="M1 3 C1 1 3 1 5 1 C7 1 9 1 9 3 L7 3.5 L6.5 2.5 L3.5 2.5 L3 3.5 Z M2.5 4 L7.5 4 L8.5 8.5 L1.5 8.5 Z" fill="var(--ink)"/></svg></li>
    <li><span>nola@theamberadvisorycollective.com.au</span>
      <svg viewBox="0 0 10 9" aria-hidden="true"><rect x="0.5" y="1" width="9" height="7" fill="var(--ink)"/><path d="M1 1.8 L5 5 L9 1.8" stroke="var(--paper)" stroke-width="0.8" fill="none"/></svg></li>
    <li><span>theamberadvisorycollective.com.au</span>
      <svg viewBox="0 0 10 9" aria-hidden="true"><rect x="0.5" y="0.5" width="9" height="6" fill="var(--ink)"/><rect x="1.6" y="1.5" width="6.8" height="4" fill="var(--paper)"/><rect x="3" y="7.3" width="4" height="1.2" fill="var(--ink)"/></svg></li>
  </ul>
</section>

</body>
</html>
```